Hi everyone,
Clear Path Homes is a business that renovates older houses into modern homes. I'm looking for a design that is clean and simple. It needs to show the client that renovating is a simple process. No more than 3 colours to be used thanks.

What I need:
1. Logo
2. Business card (one side)
3. Letter head (A4)

Looking forward to the designs!

Industry/Entity Type

Construction

Logo Text

Clear Path Homes

Font styles to use
Sans Serif

Requirements
Must have
• Trading name: Clear Path Homes
• Contact name: Daniel Whitcombe
• Email: danielwhitcombe@clearpathhomes.com.au
• Tel: 0412 758 204
• Clean and simple
Nice to have
• If design might include a few tools. eg Hammer, paint roller etc.
Should not have
• Complicated design

```html
<!DOCTYPE html>
<html lang="en">
<head>
<meta charset="utf-8">
<title>Clear Path Homes – Stationery</title>
<link rel="stylesheet" href="https://fonts.googleapis.com/css2?family=Open+Sans:wght@400;600;700;800&display=swap">
<style>
  :root {
    --navy: #1d3a5c;
    --orange: #f47b20;
    --grey: #6f7378;
    --paper: #ffffff;
    --stage: #ececec;
    --faint: #f1f1f2;
    --ink: #2b2f33;
  }
  * { box-sizing: border-box; margin: 0; padding: 0; }
  html, body { width: 1200px; height: 795px; overflow: hidden; }
  body {
    background: var(--stage);
    font-family: "Open Sans", Arial, sans-serif;
    color: var(--ink);
    position: relative;
  }

  /* ---------- Logo ---------- */
  .logo { display: inline-flex; align-items: center; gap: 0.28em; }
  .logo-name {
    font-weight: 800;
    color: var(--navy);
    line-height: 0.95;
    letter-spacing: -0.01em;
  }
  .logo-name span { display: block; }
  .logo-mark {
    width: 1.55em; height: 1.55em;
    background: var(--orange);
    border-radius: 0.18em;
    flex: none;
  }
  .logo--reverse .logo-name { color: #ffffff; }

  .brand-lockup { position: absolute; left: 70px; top: 652px; font-size: 40px; }

  /* ---------- Letterhead ---------- */
  .letterhead {
    position: absolute; left: 350px; top: 28px;
    width: 520px; height: 736px;
    background: var(--paper);
    box-shadow: 0 2px 10px rgba(0,0,0,0.08);
    padding: 44px 46px 0;
    overflow: hidden;
  }
  .letterhead-watermark {
    position: absolute; left: 190px; top: 210px;
    width: 240px; height: 240px;
    background: var(--faint);
    border-radius: 22px;
  }
  .letterhead-top { position: relative; display: flex; justify-content: space-between; align-items: flex-start; }
  .letterhead-top .logo { font-size: 17px; }
  .letter-date { font-size: 7.5px; font-weight: 700; color: var(--ink); margin-top: 2px; }

  .recipient { position: relative; margin-top: 40px; font-size: 8px; font-weight: 600; line-height: 1.45; }
  .salutation { position: relative; margin-top: 34px; font-size: 8px; font-weight: 700; }
  .letter-body { position: relative; margin-top: 12px; width: 330px; font-size: 7px; line-height: 1.55; }
  .letter-body p + p { margin-top: 12px; }
  .closing { position: relative; margin-top: 16px; font-size: 7.5px; font-weight: 700; }

  .signature-block { position: absolute; right: 46px; top: 330px; width: 110px; }
  .signer-name { font-size: 7.5px; font-weight: 700; }
  .signer-role { font-size: 6.5px; color: var(--grey); }
  .signature {
    margin-top: 6px; width: 100px; height: 30px;
    background: linear-gradient(90deg, rgba(29,58,92,0.10), rgba(29,58,92,0.22));
    border-radius: 3px;
  }

  .letterhead-footer { position: absolute; left: 0; right: 0; bottom: 0; }
  .footer-rule { height: 3px; background: var(--navy); margin: 0 46px 0; opacity: 0.85; }
  .footer-brand {
    text-align: center; font-size: 7px; font-weight: 700;
    letter-spacing: 0.08em; color: var(--orange); margin: 0 0 8px;
  }
  .footer-band {
    background: var(--navy); color: #ffffff;
    height: 26px; display: flex; align-items: center; justify-content: center;
    font-size: 6.5px; gap: 6px;
  }
  .footer-band b { font-weight: 700; }

  /* ---------- Business cards ---------- */
  .card {
    position: absolute; width: 280px; height: 160px;
    box-shadow: 0 2px 10px rgba(0,0,0,0.10);
  }
  .card--back {
    left: 900px; top: 290px; background: var(--navy);
    display: flex; align-items: center; justify-content: center;
  }
  .card--back .logo { font-size: 22px; }
  .card--front { left: 900px; top: 480px; background: var(--paper); padding: 24px 28px; }
  .card--front .logo { font-size: 17px; }
  .card-name { margin-top: 16px; font-size: 11px; font-weight: 700; color: var(--navy); }
  .card-contacts { list-style: none; margin-top: 7px; font-size: 7.5px; color: var(--ink); }
  .card-contacts li { display: flex; align-items: center; gap: 6px; line-height: 1.7; }
  .contact-icon {
    width: 10px; height: 10px; border-radius: 2px; background: var(--orange);
    display: inline-flex; align-items: center; justify-content: center; flex: none;
  }
  .contact-icon svg { width: 7px; height: 7px; }
</style>
</head>
<body>

  <!-- Letterhead -->
  <section class="letterhead">
    <div class="letterhead-watermark" aria-hidden="true"></div>

    <header class="letterhead-top">
      <div class="logo">
        <div class="logo-name"><span>Clear Path</span><span>Homes</span></div>
        <div class="logo-mark"></div>
      </div>
      <p class="letter-date">Your Town, 15. January, 2016</p>
    </header>

    <address class="recipient" style="font-style:normal">
      Mr John Johnson<br>FIRM Ltd<br>6015 Long Street<br>Stadt 7257
    </address>

    <p class="salutation">Dear Mr Johnson,</p>

    <div class="letter-body">
      <p>Fusce neque mi, consectetuer gravida, convallis ac, varius a, pede. Fusce pellentesque pretium quam. Ut luctus, justo id volutpat iaculis, est diam pulvinar sem, quis bibendum purus dui eget mauris. Sed in mauris. In massa. Pellentesque condimentum felis nec libero. Integer pulvinar elit at turpis. Nulla facilisi. Sed sapien ipsum, commodo id, facilisis vitae, ultrices non, metus. Aenean non nulla. Curabitur molestie volutpat magna. Vestibulum tempor faucibus nisi. Pellentesque vitae enim.</p>
      <p>Aliquam rhoncus volutpat mauris. Sed auctor. Donec tincidunt velit et tellus. Donec sed augue eget lacus placerat adipiscing. Ut convallis suscipit nulla. Morbi posuere ullamcorper ligula. Duis placerat eget sit amet odio. Suspendisse ante nulla, gravida quis, eleifend sit amet, tempor tempus.</p>
      <p>In ante. Phasellus convallis, nisl in vestibulum facilisis, lacus pede bibendum urna, dapibus pellentesque est a metus. Etiam tortor arcu, porta nec, laoreet quis, mollis in, libero. Vivamus euismod, odio id mattis porttitor, tellus nisi consectetuer turpis, ut auctor enim justo euismod nulla. Sed auctor.</p>
    </div>

    <p class="closing">Mit freundlichen Grüßen,</p>

    <div class="signature-block">
      <p class="signer-name">Daniel Whitcombe</p>
      <p class="signer-role">Director</p>
      <div class="signature" role="img" aria-label="Handwritten signature of Daniel Whitcombe"></div>
    </div>

    <footer class="letterhead-footer">
      <p class="footer-brand">CLEAR PATH HOMES</p>
      <div class="footer-band">
        <span>20 Street, Town 7224</span>•
        <span><b>Phone:</b> 0412 758 204</span>•
        <span><b>E-Mail:</b> danielwhitcombe@clearpathhomes.com.au</span>•
        <span><b>Website:</b> www.clearpathhomes.com.au</span>
      </div>
    </footer>
  </section>

  <!-- Business card, back -->
  <section class="card card--back">
    <div class="logo logo--reverse">
      <div class="logo-name"><span>Clear Path</span><span>Homes</span></div>
      <div class="logo-mark"></div>
    </div>
  </section>

  <!-- Business card, front -->
  <section class="card card--front">
    <div class="logo">
      <div class="logo-name"><span>Clear Path</span><span>Homes</span></div>
      <div class="logo-mark"></div>
    </div>
    <p class="card-name">Daniel Whitcombe</p>
    <ul class="card-contacts">
      <li>
        <span class="contact-icon"><svg viewBox="0 0 10 10"><path d="M2 1h2l1 2.5-1.2.8a5 5 0 0 0 2 2l.8-1.2L9 6v2a1 1 0 0 1-1 1A7 7 0 0 1 1 2a1 1 0 0 1 1-1z" fill="#fff"/></svg></span>
        0412 758 204
      </li>
      <li>
        <span class="contact-icon"><svg viewBox="0 0 10 10"><rect x="1" y="2" width="8" height="6" fill="none" stroke="#fff" stroke-width="1"/><path d="M1 2l4 3.5L9 2" fill="none" stroke="#fff" stroke-width="1"/></svg></span>
        danielwhitcombe@clearpathhomes.com.au
      </li>
      <li>
        <span class="contact-icon"><svg viewBox="0 0 10 10"><circle cx="5" cy="5" r="3.8" fill="none" stroke="#fff" stroke-width="1"/><path d="M1.2 5h7.6M5 1.2c-2 2.5-2 5.1 0 7.6M5 1.2c2 2.5 2 5.1 0 7.6" fill="none" stroke="#fff" stroke-width="0.8"/></svg></span>
        www.clearpathhomes.com.au
      </li>
    </ul>
  </section>

  <!-- Standalone brand lockup -->
  <div class="brand-lockup">
    <div class="logo">
      <div class="logo-name"><span>Clear Path</span><span>Homes</span></div>
      <div class="logo-mark"></div>
    </div>
  </div>

</body>
</html>
```